Webdesign für die Korvelt GmbH
Zielgruppe
Beratung • Renovierung • Reparatur • Planung • Bau • Pflege • Wartung im Bereich der Haustechnik
Aufgabenstellung
Bilder nur von bildmoro oder von der Webseite des Kunden nutzen

```html
<!DOCTYPE html>
<html lang="de">
<head>
<meta charset="utf-8">
<title>Korvelt GmbH – Haustechnik</title>
<link rel="stylesheet" href="https://fonts.googleapis.com/css2?family=Open+Sans:wght@400;600;700&display=swap">
<style>
  :root {
    --sky: #bde0f2;
    --white: #ffffff;
    --brand-blue: #0a8fe6;
    --dot-light: #a8d4f0;
    --accent-red: #e2261c;
    --pool-tone: #dfe9f3;
    --stone-tone: #ece8e0;
    --tub-tone: #c9cde6;
    --card-glow: rgba(90, 170, 225, 0.55);
  }
  * { box-sizing: border-box; margin: 0; padding: 0; }
  html, body { width: 1200px; height: 675px; overflow: hidden; }
  body {
    position: relative;
    font-family: "Open Sans", sans-serif;
    background: linear-gradient(180deg, var(--sky) 0%, #d4ebf6 45%, var(--white) 100%);
  }
  .site-card {
    position: absolute;
    left: 71px; top: 59px;
    width: 1051px; height: 557px;
    border-radius: 26px;
    overflow: hidden;
    background: var(--white);
    box-shadow: 0 0 14px var(--card-glow);
  }
  .hero-backdrop {
    position: absolute; inset: 0 0 auto 0; height: 420px;
    background:
      linear-gradient(180deg, rgba(255,255,255,0) 30%, var(--white) 100%),
      linear-gradient(100deg, var(--pool-tone) 0%, #e6edf4 42%, var(--stone-tone) 48%, #efece6 100%);
  }
  .brand {
    position: absolute; left: 72px; top: 63px;
    display: flex; align-items: center; gap: 8px;
    color: var(--brand-blue);
    font-weight: 700; font-size: 21px; letter-spacing: 0.5px;
  }
  .brand-mark { width: 12px; height: 12px; background: var(--brand-blue); }
  .toolbar { position: absolute; right: 46px; top: 71px; display: flex; gap: 10px; align-items: center; }
  .tub-photo {
    position: absolute; left: 513px; top: 124px;
    width: 457px; height: 287px;
    background: radial-gradient(ellipse at 50% 55%, var(--tub-tone) 0%, #dde0ef 55%, rgba(255,255,255,0) 78%);
  }
  .slide-dots { position: absolute; left: 1012px; top: 217px; display: flex; flex-direction: column; gap: 25px; }
  .slide-dot { width: 13px; height: 13px; border-radius: 50%; border: 2.5px solid var(--brand-blue); }
  .slide-dot.is-active { border-color: var(--dot-light); }
  .welcome { position: absolute; left: 112px; top: 219px; width: 426px; color: var(--brand-blue); }
  .welcome-title { font-size: 16px; font-weight: 700; letter-spacing: 0.2px; margin-left: 71px; }
  .welcome-text { margin-top: 27px; font-size: 15.4px; line-height: 23.8px; margin-left: 26px; }
  .scroll-hint {
    position: absolute; left: 50%; top: 486px; transform: translateX(-50%);
    display: flex; flex-direction: column; align-items: center; gap: 2px;
    color: var(--accent-red); font-size: 16px;
  }
</style>
</head>
<body>
  <main class="site-card">
    <div class="hero-backdrop" role="img" aria-label="Helles Foto eines Schwimmbeckenrands mit Wasserspiegelung"></div>

    <div class="brand"><span class="brand-mark"></span>KORVELT</div>

    <nav class="toolbar" aria-label="Werkzeuge">
      <svg width="26" height="26" viewBox="0 0 26 26" aria-label="Suche">
        <circle cx="11" cy="11" r="8.5" fill="none" stroke="var(--brand-blue)" stroke-width="2.6"/>
        <line x1="17.3" y1="17.3" x2="23.5" y2="23.5" stroke="var(--brand-blue)" stroke-width="2.8" stroke-linecap="round"/>
      </svg>
      <svg width="34" height="22" viewBox="0 0 34 22" aria-label="Menü">
        <line x1="1" y1="3" x2="27" y2="3" stroke="var(--brand-blue)" stroke-width="2.6" stroke-linecap="round"/>
        <line x1="7" y1="11" x2="33" y2="11" stroke="var(--brand-blue)" stroke-width="2.6" stroke-linecap="round"/>
        <line x1="1" y1="19" x2="27" y2="19" stroke="var(--brand-blue)" stroke-width="2.6" stroke-linecap="round"/>
      </svg>
    </nav>

    <div class="tub-photo" role="img" aria-label="Freistehende weiße Badewanne mit Standarmatur und Handtuch"></div>

    <div class="slide-dots" aria-label="Folien">
      <span class="slide-dot is-active"></span>
      <span class="slide-dot"></span>
      <span class="slide-dot"></span>
      <span class="slide-dot"></span>
    </div>

    <section class="welcome">
      <h1 class="welcome-title">HERZLICH WILLKOMMEN</h1>
      <p class="welcome-text">Wenn Sie einen zuverlässigen Partner für die Erledigung Ihrer Aufträge suchen, Wert auf Kreativität und Freundlichkeit legen, dann sind Sie bei uns an der richtigen Stelle. Vom ersten Beratungsgespräch bis zur Übergabe der fertiggestellten Leistung, sollten Sie, wie viele Kunden vor Ihnen, gute Erfahrungen mit uns machen.</p>
    </section>

    <div class="scroll-hint">
      <span>Scroll down</span>
      <svg width="18" height="20" viewBox="0 0 18 20" aria-hidden="true">
        <polyline points="2,2 9,8 16,2" fill="none" stroke="var(--accent-red)" stroke-width="2.4"/>
        <polyline points="2,11 9,17 16,11" fill="none" stroke="var(--accent-red)" stroke-width="2.4"/>
      </svg>
    </div>
  </main>
</body>
</html>
```